Business card for plumber

I need a business card for my plumbing company.
on it should:
Surname
position
E-mail
Telephone & mobile phone
Website
Please everything as placeholders / fantasy names.
We stand for high quality, hygiene and professionalism.

Colours:
# 606060 anthracite
# f7931e orange
# 2b89cc blue

Industry/Entity Type

Plumber

Contact Information for Business Card

folgt...

```html
<!DOCTYPE html>
<html lang="en">
<head>
<meta charset="utf-8">
<title>Brennwald Haustechnik – Business Card</title>
<link href="https://fonts.googleapis.com/css2?family=Roboto:ital,wght@0,400;0,700;1,400&display=swap" rel="stylesheet">
<style>
  :root {
    --backdrop: #2b2b2b;
    --card: #1d1d1e;
    --anthracite: #606060;
    --orange: #f7931e;
    --blue: #2b89cc;
    --white: #f2f2f2;
    --emboss: #262627;
  }
  * { margin: 0; padding: 0; box-sizing: border-box; }
  html, body { width: 1200px; height: 900px; overflow: hidden; }
  body {
    background: var(--backdrop);
    font-family: "Roboto", Arial, sans-serif;
    color: var(--white);
    position: relative;
  }
  .card {
    position: absolute;
    left: 250px;
    width: 700px;
    height: 400px;
    background: var(--card);
    overflow: hidden;
    box-shadow: 0 10px 30px rgba(0,0,0,.45);
  }
  .card--front { top: 35px; }
  .card--back { top: 465px; }

  /* front */
  .brand {
    position: absolute;
    left: 60px;
    top: 55px;
    display: flex;
    align-items: center;
    gap: 12px;
  }
  .brand__dot {
    width: 34px; height: 34px;
    border-radius: 50%;
    background: var(--orange);
  }
  .brand__name {
    font-weight: 700;
    font-size: 26px;
    letter-spacing: 1px;
    color: var(--blue);
    text-transform: uppercase;
  }
  .person { position: absolute; left: 60px; top: 145px; }
  .person__name {
    font-weight: 700;
    font-size: 30px;
    color: var(--blue);
    text-transform: uppercase;
    letter-spacing: .5px;
  }
  .person__role {
    font-style: italic;
    font-size: 17px;
    margin-top: 4px;
  }
  .contacts {
    position: absolute;
    left: 60px;
    top: 235px;
    list-style: none;
    font-size: 17px;
    line-height: 29px;
  }
  .contacts li { display: flex; align-items: center; gap: 12px; }
  .contacts svg { width: 15px; height: 15px; fill: var(--orange); flex: none; }
  .emboss {
    position: absolute;
    right: -40px;
    bottom: -60px;
    width: 360px;
    height: 360px;
    border-radius: 50%;
    background: var(--emboss);
    box-shadow: inset 2px 2px 4px rgba(255,255,255,.04), inset -3px -3px 6px rgba(0,0,0,.35);
  }

  /* back */
  .back-brand {
    position: absolute;
    right: 70px;
    top: 95px;
    display: flex;
    align-items: center;
    gap: 12px;
  }
  .tagline {
    position: absolute;
    left: 60px;
    bottom: 60px;
    font-size: 17px;
    letter-spacing: .5px;
    text-transform: uppercase;
  }
</style>
</head>
<body>
  <section class="card card--front">
    <div class="brand">
      <span class="brand__dot"></span>
      <span class="brand__name">Brennwald Haustechnik</span>
    </div>
    <div class="person">
      <div class="person__name">Jonas Keller</div>
      <div class="person__role">President</div>
    </div>
    <ul class="contacts">
      <li><svg viewBox="0 0 16 16"><path d="M3 1l3 3-2 2c1 2 4 5 6 6l2-2 3 3-2 2C7 15 1 9 1 3z"/></svg>555 210 4433</li>
      <li><svg viewBox="0 0 16 16"><path d="M4 0h8a1 1 0 0 1 1 1v14a1 1 0 0 1-1 1H4a1 1 0 0 1-1-1V1a1 1 0 0 1 1-1zm1 2v10h6V2z"/></svg>555 210 4433</li>
      <li><svg viewBox="0 0 16 16"><path d="M0 3h16v10H0zm1 1v1l7 5 7-5V4z"/></svg>info@brennwaldhaustec.com</li>
      <li><svg viewBox="0 0 16 16"><circle cx="8" cy="8" r="7.5"/></svg>www.brennwaldhaustec.com</li>
    </ul>
    <div class="emboss" role="img" aria-label="Faint embossed brand decoration"></div>
  </section>

  <section class="card card--back">
    <div class="back-brand">
      <span class="brand__dot"></span>
      <span class="brand__name">Brennwald Haustechnik</span>
    </div>
    <p class="tagline">We stand for high quality, hygiene and professionalism.</p>
  </section>
</body>
</html>
```